Insurance Company Website Design

We are working with an insurance company. They sell home, auto, commercial, and health insurance. We like the "get a quote" in the banner of https://www.plovanta.example and https://www.quirelmog.example.

Some sites to use for content/competitors and inspiration:
https://velturbrookins.example
https://kamzubredainsurance.example
https://tvorpinsurance.example
https://www.insuranceforzelmarids.example
https://www.plovanta.example
https://www.quirelmog.example

Thank you for taking the time to consider designing a website for us. We are web developers based in Stockton, CA, USA. Most of our projects go through the same process. Understanding this process may help you win a project with us. We custom-code all of our websites in-house. We don’t have any requirements as to what tools you use for your design, but we ask that you follow these guidelines.

IMAGES:
If you use any images or icons in the design, we ask that you have a link to the asset so we can purchase the image/icon. Most of the designs we submit do not have the customer’s images on them unless they have some great images. Be creative; show us the feeling you are trying to portray with your image choices. Use any royalty-free site you choose. We subscribe to Quintrel and mainly use their images, but we can purchase images outside of Quintrel. PLEASE NOTE: we will not submit designs to clients with watermarks on the images.

FONTS:
We ask that you identify the fonts you’re using in the design. This can be done in a message if you want. We typically use Google Fonts and Quintrel Fonts.

CONTENT:
We're always open to different content and ideas. We often submit designs with stock images so the client can see our vision. We typically take pictures after the website launch to use their images with our vision. Lorem Ipsum is fine for paragraphs, but we ask that you make the Headers with correct English. We want to be able to show the vision and identify the sections of the website.

INSPIRATION:
We typically add a couple of links in the brief of websites we like to help you get started in your design.

REVISIONS:
We do not often ask for revisions of the designs unless we see something in the design that may not appeal to the client. If there are slight changes that we want to make, we do that in the development process.

FEEDBACK:
We rarely give feedback on designs during the design process. We are working on many website projects and do not have the time to provide feedback. We usually respond if your request is well thought out and asks specific questions, but a note asking “feedback, please” usually goes unanswered.

```html
<!DOCTYPE html>
<html lang="en">
<head>
<meta charset="utf-8">
<title>Canopira Insurance</title>
<link href="https://fonts.googleapis.com/css2?family=Poppins:ital,wght@0,300;0,400;0,500;0,600;1,500&display=swap" rel="stylesheet">
<style>
:root{
  --blue:#0a6fc2;
  --blue-bright:#1a8ad9;
  --ink:#333;
  --muted:#666;
  --soft:#f7f7f7;
  --card:#f4f4f4;
  --dark:#2b2d31;
  --white:#fff;
  --star:#f5b400;
}
*{margin:0;padding:0;box-sizing:border-box}
html,body{width:1200px;height:3680px;overflow:hidden}
body{font-family:'Poppins',sans-serif;color:var(--ink);background:var(--white);position:relative}
a{color:inherit;text-decoration:none}

/* header */
.site-header{position:absolute;left:0;top:0;width:1200px;height:129px;background:var(--white)}
.brand{position:absolute;left:86px;top:40px;display:flex;align-items:center;gap:12px;font-size:40px;font-weight:400;color:var(--blue);line-height:48px}
.brand-dot{width:24px;height:24px;border-radius:50%;background:var(--blue)}
.main-nav{position:absolute;left:420px;top:50px;display:flex;gap:24px;font-size:15px;color:#555}
.main-nav .active{color:var(--blue);font-weight:500}
.btn{display:inline-flex;align-items:center;justify-content:center;background:var(--blue);color:var(--white);font-size:17px}
.contact-btn{position:absolute;left:997px;top:44px;width:117px;height:39px;font-size:16px}

/* hero */
.hero{position:absolute;left:0;top:129px;width:1200px;height:682px;background:linear-gradient(100deg,#2a2b2e 0%,#3b3836 40%,#4a3f3a 60%,#2e2c2b 100%)}
.hero-title{position:absolute;left:83px;top:198px;font-size:54px;font-weight:400;line-height:57px;color:var(--white)}
.hero-text{position:absolute;left:86px;top:330px;width:500px;font-size:15.5px;line-height:24px;color:var(--white)}
.hero-btn{position:absolute;left:86px;top:432px;width:143px;height:45px}
.quote-frame{position:absolute;left:684px;top:115px;width:399px;height:449px;border:7px solid #4a4a4a}
.quote-panel{position:absolute;left:0;top:0;width:385px;height:435px;background:var(--blue);color:var(--white)}
.quote-panel h2{position:absolute;left:42px;top:66px;font-size:27px;font-weight:400}
.quote-panel p{position:absolute;left:44px;top:111px;width:300px;font-size:15px;line-height:24px}
.field{position:absolute;left:45px;width:245px;height:46px;background:var(--white);color:var(--blue);font-size:14px;padding-left:22px;display:flex;align-items:center}
.field.select{top:196px;justify-content:space-between;padding-right:16px}
.field.zip{top:253px}
.quote-btn{position:absolute;left:45px;top:319px;width:247px;height:47px;border:2px solid var(--white);border-radius:24px;display:flex;align-items:center;justify-content:center;font-size:18px;font-weight:500}

/* products */
.products{position:absolute;left:0;top:813px;width:1200px;height:534px;background:var(--soft)}
.section-title{position:absolute;left:0;width:1200px;text-align:center;font-size:43px;font-weight:400;color:var(--blue)}
.products .section-title{top:64px}
.products .lead{position:absolute;left:0;top:124px;width:1200px;text-align:center;font-size:15.5px;line-height:23px;color:#555}
.product{position:absolute;top:214px;width:240px;margin-left:-120px;text-align:center}
.product-icon{width:98px;height:98px;margin:0 auto;border-radius:50%;border:2px dotted var(--blue);display:flex;align-items:center;justify-content:center}
.product-icon span{width:82px;height:82px;border-radius:50%;background:var(--blue);display:flex;align-items:center;justify-content:center}
.product h3{margin-top:30px;font-size:18px;font-weight:400;color:var(--blue)}
.product p{margin-top:12px;font-size:14px;line-height:22px;color:#555;padding:0 12px}

/* about */
.about{position:absolute;left:0;top:1347px;width:1200px;height:643px;background:var(--white)}
.about h2{position:absolute;left:84px;top:110px;font-size:43px;font-weight:400;color:var(--blue)}
.about-copy{position:absolute;left:84px;top:198px;width:625px;font-size:15px;line-height:24px;color:#555}
.about-copy p{margin-bottom:24px}
.about-btn{position:absolute;left:84px;top:476px;width:142px;height:47px}
.about-photo{position:absolute;left:753px;top:57px;width:361px;height:530px;border-radius:12px;background:linear-gradient(160deg,#3e5f7c 0%,#a59887 45%,#d8d2cb 70%,#7a5a3f 100%)}

/* comparison */
.compare{position:absolute;left:0;top:1990px;width:1200px;height:704px;background:linear-gradient(180deg,#303236,#24262a)}
.compare .section-title{top:56px;color:var(--white)}
.compare-table{position:absolute;left:43px;top:146px;width:1114px;border-collapse:collapse;color:var(--white)}
.compare-table th,.compare-table td{border:1px solid #8a8c90;vertical-align:middle}
.compare-table th{height:71px;font-size:26px;font-weight:400;color:var(--blue-bright);text-align:left;padding-left:40px}
.compare-table td{font-size:18.5px;line-height:26px;padding-left:43px}
.compare-table td.mark{text-align:center;padding:0}
.compare-table td.note{font-size:15.5px;line-height:25px;padding-left:34px}
.compare-table td.note2{font-size:15.5px;line-height:25px;padding-left:12px}
.dash{display:inline-block;width:22px;height:4px;background:var(--white)}
.compare-btn{position:absolute;left:523px;top:607px;width:153px;height:44px;font-size:18px}

/* testimonials */
.testimonials{position:absolute;left:0;top:2694px;width:1200px;height:509px;background:var(--white)}
.testimonials .section-title{top:74px}
.t-card{position:absolute;top:160px;width:451px;height:263px;background:var(--card);text-align:center}
.avatar{width:72px;height:72px;border-radius:50%;margin:17px auto 0;background:linear-gradient(135deg,#8a7b6e,#c9b8a6)}
.stars{margin-top:8px;color:var(--star);font-size:15px;letter-spacing:1px}
.t-name{font-size:18px;color:#333;margin-top:2px}
.t-role{font-size:14.5px;font-style:italic;font-weight:500;color:var(--blue)}
.t-text{margin:16px auto 0;width:400px;font-size:14px;line-height:21px;color:#777}
.arrow{position:absolute;top:2963px;width:46px;height:46px;border-radius:50%;background:var(--blue);display:flex;align-items:center;justify-content:center}

/* footer */
.site-footer{position:absolute;left:0;top:3203px;width:1200px;height:477px;background:linear-gradient(135deg,#1676c6,#0e66b6 50%,#1a78c8);color:var(--white)}
.f-col{position:absolute;top:103px}
.f-col h4{font-size:20px;font-weight:400}
.f-col h4 b{font-weight:600}
.f-col .rule{width:40px;height:3px;background:var(--white);margin-top:8px}
.f-links{list-style:none;margin-top:38px;font-size:16px}
.f-links li{height:31px;display:flex;align-items:center;gap:12px}
.contact-item{position:absolute;left:723px;display:flex;gap:18px;font-size:16px;line-height:22px}
.c-icon{width:33px;height:33px;border:1.5px solid var(--white);border-radius:5px;display:flex;align-items:center;justify-content:center;flex:none}
.f-rule{position:absolute;left:83px;top:388px;width:1031px;height:1px;background:rgba(255,255,255,.5)}
.social{position:absolute;top:412px;width:43px;height:43px;border:2px solid var(--white);border-radius:50%}
.copyright{position:absolute;right:89px;top:423px;font-size:16px}
</style>
</head>
<body>

<header class="site-header">
  <div class="brand"><span class="brand-dot"></span>canopira</div>
  <nav class="main-nav">
    <a class="active">Home</a><a>About Us</a><a>Our Services</a><a>Latest Blogs</a><a>Our Testimonials</a>
  </nav>
  <a class="btn contact-btn">Contact Us</a>
</header>

<section class="hero" role="img" aria-label="Photo of an older couple reviewing insurance papers at home">
  <h1 class="hero-title">Affordable Insurance<br>Just For You</h1>
  <p class="hero-text">The Lake Corvane Foundation is a great way to events to see what fun things LCA has planned!The Lake Corvane Foundation is hat fun things LCA has planned!</p>
  <a class="btn hero-btn">Our Mission</a>
  <div class="quote-frame">
    <form class="quote-panel">
      <h2>Insurance quote online.</h2>
      <p>Introducing the Quirelmog® Personal Price Plan®</p>
      <div class="field select">Home
        <svg width="12" height="8" viewBox="0 0 12 8"><path d="M1 1l5 5 5-5" fill="none" stroke="#0a6fc2" stroke-width="1.8"/></svg>
      </div>
      <div class="field zip">Zip Code</div>
      <div class="quote-btn">GET A QUOTE</div>
    </form>
  </div>
</section>

<section class="products">
  <h2 class="section-title">Our Most Popular Insurance Products</h2>
  <p class="lead">Being independent means that we find the best companies and products for our<br>customers – not customers to force-fit into proprietary products.</p>

  <div class="product" style="left:214px">
    <div class="product-icon"><span>
      <svg width="38" height="42" viewBox="0 0 38 42"><path d="M19 2l15 6v12c0 10-7 17-15 20C11 37 4 30 4 20V8z" fill="#fff"/><path d="M19 12l2.6 5.4 5.9.8-4.3 4.1 1 5.8-5.2-2.8-5.2 2.8 1-5.8-4.3-4.1 5.9-.8z" fill="none" stroke="#0a6fc2" stroke-width="1.8"/></svg>
    </span></div>
    <h3>HOME INSURANCE</h3>
    <p>Homeowners insurance can help protect you from the unexpected.</p>
  </div>

  <div class="product" style="left:463px">
    <div class="product-icon"><span>
      <svg width="46" height="44" viewBox="0 0 46 44"><g fill="#fff"><circle cx="18" cy="26" r="11"/><g stroke="#fff" stroke-width="5"><path d="M18 11v30M3 26h30M7.4 15.4l21.2 21.2M28.6 15.4L7.4 36.6"/></g><circle cx="34" cy="12" r="6"/><g stroke="#fff" stroke-width="3"><path d="M34 3v18M25 12h18M27.6 5.6l12.8 12.8M40.4 5.6L27.6 18.4"/></g></g><circle cx="18" cy="26" r="4.5" fill="#0a6fc2"/><circle cx="34" cy="12" r="2.5" fill="#0a6fc2"/></svg>
    </span></div>
    <h3>AUTO INSURANCE</h3>
    <p>We work with all of the top Start comparing rates in just minutes!</p>
  </div>

  <div class="product" style="left:719px">
    <div class="product-icon"><span>
      <svg width="46" height="46" viewBox="0 0 46 46"><g fill="none" stroke="#fff" stroke-width="2.4"><ellipse cx="23" cy="23" rx="20" ry="8"/><ellipse cx="23" cy="23" rx="20" ry="8" transform="rotate(60 23 23)"/><ellipse cx="23" cy="23" rx="20" ry="8" transform="rotate(120 23 23)"/></g><circle cx="23" cy="23" r="4" fill="#fff"/></svg>
    </span></div>
    <h3>COMMERCIAL INSURANCE</h3>
    <p>Protecting personal possessions with a Renter's Insurance policy today.</p>
  </div>

  <div class="product" style="left:980px">
    <div class="product-icon"><span>
      <svg width="46" height="44" viewBox="0 0 46 44"><g fill="#fff"><circle cx="18" cy="26" r="11"/><g stroke="#fff" stroke-width="5"><path d="M18 11v30M3 26h30M7.4 15.4l21.2 21.2M28.6 15.4L7.4 36.6"/></g><circle cx="34" cy="12" r="6"/><g stroke="#fff" stroke-width="3"><path d="M34 3v18M25 12h18M27.6 5.6l12.8 12.8M40.4 5.6L27.6 18.4"/></g></g><circle cx="18" cy="26" r="4.5" fill="#0a6fc2"/><circle cx="34" cy="12" r="2.5" fill="#0a6fc2"/></svg>
    </span></div>
    <h3>HEALTH INSURANCE</h3>
    <p>Velturbrook Insurance helps you find health coverage that fits your needs and budget.</p>
  </div>
</section>

<section class="about">
  <h2>We are Here for You Stay Cool.</h2>
  <div class="about-copy">
    <p>With different regions, topography, and climates from the Red to the Rio Grande River, our state is certainly anything but predictable, and that can cause you to get more familiar with Texas home insurance than you ever expected.</p>
    <p>With the number of new Texas homeowners, businesses relocating or starting, and automobile drivers continuing to increase, having the right insurance cover-age for each is also a big deal.</p>
    <p>One thing is for certain when you partner with us for coverage . . . you are never alone when it comes to securing you and yours.</p>
  </div>
  <a class="btn about-btn">Read More</a>
  <div class="about-photo" role="img" aria-label="Photo of a young woman at a kitchen table reviewing documents beside a laptop and mug"></div>
</section>

<section class="compare" role="region" aria-label="Coverage comparison">
  <h2 class="section-title">Finding The Best Coverage For You</h2>
  <table class="compare-table">
    <colgroup><col style="width:401px"><col style="width:206px"><col style="width:237px"><col style="width:270px"></colgroup>
    <tr><th>Features &amp; Services</th><th style="padding-left:26px">Our Agency</th><th style="padding-left:35px">Captive Agent</th><th style="padding-left:12px">Online Company</th></tr>
    <tr style="height:89px"><td>Access to multiple companies and<br>wide range of products</td>
      <td class="mark"><svg width="26" height="22" viewBox="0 0 26 22"><path d="M2 12l7 7L24 3" fill="none" stroke="#fff" stroke-width="4"/></svg></td>
      <td class="mark"><span class="dash"></span></td><td class="mark"><span class="dash"></span></td></tr>
    <tr style="height:85px"><td>Easy switching from company to<br>company without hassle</td>
      <td class="mark"><svg width="26" height="22" viewBox="0 0 26 22"><path d="M2 12l7 7L24 3" fill="none" stroke="#fff" stroke-width="4"/></svg></td>
      <td class="note">Tries to sell &amp; support<br>only their one company</td><td class="mark"><span class="dash"></span></td></tr>
    <tr style="height:86px"><td>Unbiased and objective advice</td>
      <td class="mark"><svg width="26" height="22" viewBox="0 0 26 22"><path d="M2 12l7 7L24 3" fill="none" stroke="#fff" stroke-width="4"/></svg></td>
      <td class="note">Adjusters exclusive to<br>the one company</td><td class="note2">No help: you vs. adjuster<br>&nbsp;</td></tr>
    <tr style="height:93px"><td>Claims assistance and advocacy</td>
      <td class="mark"><svg width="26" height="22" viewBox="0 0 26 22"><path d="M2 12l7 7L24 3" fill="none" stroke="#fff" stroke-width="4"/></svg></td>
      <td class="note">Often passed off to<br>call center</td><td class="note2">You'll likely never talk to<br>the same person twice</td></tr>
  </table>
  <a class="btn compare-btn">Get A Quote</a>
</section>

<section class="testimonials">
  <h2 class="section-title">What Our Clients Says</h2>
  <article class="t-card" style="left:139px">
    <div class="avatar" role="img" aria-label="Portrait of a client"></div>
    <div class="stars">★★★★★</div>
    <div class="t-name">Dalen Morrow</div>
    <div class="t-role">Managing director</div>
    <p class="t-text">We don't place you into a loan profile each customer as an formula created by the banking industryprofile each cus formula created by the banking industry.</p>
  </article>
  <article class="t-card" style="left:610px">
    <div class="avatar" role="img" aria-label="Portrait of a client"></div>
    <div class="stars">★★★★★</div>
    <div class="t-name">Brielle Tamsin</div>
    <div class="t-role">Organiser</div>
    <p class="t-text">We don't place you into a loan profile each customer as an formula created by the banking industryprofile each cus formula created by the banking industry.</p>
  </article>
</section>
<div class="arrow" style="left:63px"><svg width="20" height="14" viewBox="0 0 20 14"><path d="M19 7H2M8 1L2 7l6 6" fill="none" stroke="#fff" stroke-width="2.2"/></svg></div>
<div class="arrow" style="left:1093px"><svg width="20" height="14" viewBox="0 0 20 14"><path d="M1 7h17M12 1l6 6-6 6" fill="none" stroke="#fff" stroke-width="2.2"/></svg></div>

<footer class="site-footer">
  <div class="f-col" style="left:173px">
    <h4><b>Quick</b> Links</h4><div class="rule"></div>
    <ul class="f-links">
      <li>›&nbsp;Home</li><li>›&nbsp;About Us</li><li>›&nbsp;Our Services</li><li>›&nbsp;Our Blogs</li><li>›&nbsp;Testimonials</li>
    </ul>
  </div>
  <div class="f-col" style="left:454px">
    <h4><b>Customer</b> Services</h4><div class="rule"></div>
    <ul class="f-links">
      <li>›&nbsp;Home</li><li>›&nbsp;Auto</li><li>›&nbsp;Commercial</li><li>›&nbsp;Health Insurance</li>
    </ul>
  </div>
  <div class="f-col" style="left:723px;top:101px">
    <h4><b>Our</b> Newsletter</h4>
  </div>
  <div class="contact-item" style="top:197px">
    <span class="c-icon"><svg width="16" height="16" viewBox="0 0 16 16"><path d="M4 1l3 3-2 2c1 2 3 4 5 5l2-2 3 3-2 3C7 15 1 9 1 3z" fill="none" stroke="#fff" stroke-width="1.4"/></svg></span>
    <div>CALL US<br>(555) 014-2290</div>
  </div>
  <div class="contact-item" style="top:248px">
    <span class="c-icon"><svg width="16" height="12" viewBox="0 0 16 12"><rect x="1" y="1" width="14" height="10" fill="none" stroke="#fff" stroke-width="1.4"/><path d="M1 1l7 6 7-6" fill="none" stroke="#fff" stroke-width="1.4"/></svg></span>
    <div>EMAIL US<br>hello@harnwickstudio.example</div>
  </div>
  <div class="contact-item" style="top:314px">
    <span class="c-icon"><svg width="14" height="18" viewBox="0 0 14 18"><path d="M7 17S1 10 1 6.5a6 6 0 0112 0C13 10 7 17 7 17z" fill="none" stroke="#fff" stroke-width="1.4"/><circle cx="7" cy="6.5" r="2" fill="#fff"/></svg></span>
    <div>Harnwick Studio, LLC<br>2280 Orchard Vale Dr.Ste. 410 Fernmoor,<br>MD 20900</div>
  </div>
  <div class="f-rule"></div>
  <span class="social" style="left:88px"></span>
  <span class="social" style="left:139px"></span>
  <span class="social" style="left:190px"></span>
  <span class="social" style="left:242px"></span>
  <div class="copyright">All Rights Reserved @ Copyrights 2023</div>
</footer>

</body>
</html>
```